Leadership Brenvale Brochure Design*

We host a local leadership development program every two years. We need a brochure to promote the program. We would like it to be 8 1/2 x 11, tri-fold. I have attached a Word document with the necessary info for the brochure. The brochure will be professionally printed. We would like the final design to be in InDesign.

Target Market(s)

Potential participants of our leadership program. They will be local leaders, male and female, from 30-60 years of age.

Requirements
Must have
• Content as detailed in the Word document attached. Our logo.
Nice to have
• A design that is attractive to young professionals.

```html
<!DOCTYPE html>
<html lang="en">
<head>
<meta charset="utf-8">
<title>Leadership Brenvale Brochure</title>
<link href="https://fonts.googleapis.com/css2?family=Cabin:ital,wght@0,400;0,600;0,700;1,400;1,600&display=swap" rel="stylesheet">
<style>
  :root{
    --orange:#f58a2e;
    --royal:#1f43e0;
    --navy-text:#2340d6;
    --cyan:#50d9fa;
    --sky:#3fb4ee;
    --white:#ffffff;
    --sheet-shadow:0 6px 10px rgba(0,0,0,.18);
  }
  *{box-sizing:border-box;margin:0;padding:0}
  html,body{width:848px;height:1200px;overflow:hidden;background:var(--white)}
  body{position:relative;font-family:"Cabin",sans-serif;color:var(--navy-text)}
  .spread{position:absolute;left:103px;width:627px;height:463px;box-shadow:var(--sheet-shadow);background:var(--white)}
  .spread--outside{top:66px}
  .spread--inside{top:566px}
  .panel{position:absolute;top:0;width:209px;height:100%}
  .panel--1{left:0}.panel--2{left:209px}.panel--3{left:418px}

  /* outside */
  .testimonials{background:var(--orange);padding:21px 22px 0 22px;color:var(--white)}
  .section-title{font-weight:700;font-size:9.4px;color:var(--sky);margin-bottom:6px}
  .testimonials .section-title{color:var(--royal)}
  .quote{font-style:italic;font-size:8.1px;line-height:12.1px}
  .attribution{text-align:right;font-weight:600;font-size:8.1px;line-height:12.2px;margin:8px 0 12px}
  .info{padding:21px 22px 0 22px;font-size:8.2px;line-height:12.1px}
  .info p{margin-bottom:12px}
  .info strong{font-weight:700;color:var(--royal)}
  .info .section-title{margin-top:2px;margin-bottom:4px}
  .contact{text-align:center;color:var(--sky);font-weight:700;font-size:9.2px;line-height:15.5px;margin-top:2px}
  .mini-name{display:flex;align-items:center;justify-content:center;gap:4px;margin-top:10px;font-weight:700;font-size:7px;color:var(--royal)}
  .dot{display:inline-block;border-radius:50%;background:var(--orange)}
  .cover-band{position:absolute;left:0;top:0;width:209px;height:276px;background:var(--royal);display:flex;align-items:center;justify-content:center;padding:0 22px}
  .cover-quote{font-style:italic;font-weight:600;font-size:10.3px;line-height:13.6px;color:var(--orange);text-align:center;margin-top:-34px}
  .wordmark{position:absolute;left:0;top:318px;width:209px;display:flex;align-items:center;justify-content:center;gap:7px;font-weight:700;font-size:15.5px;color:var(--royal)}
  .sponsors{position:absolute;left:0;top:398px;width:209px;text-align:center;font-size:7.6px;line-height:13.6px}
  .sponsors b{font-weight:700}

  /* inside */
  .photo{position:absolute;left:0;top:0;width:209px;height:115px;background:linear-gradient(160deg,#b9a890 0%,#8c7b6a 45%,#5d6470 100%)}
  .about{position:absolute;left:0;top:115px;width:209px;height:348px;background:var(--cyan);color:var(--white);padding:25px 22px 0 22px}
  .about-lead{font-size:11.4px;line-height:12.4px;margin-bottom:10px}
  .about-lead b{font-weight:700}
  .about p{font-size:8.8px;line-height:12.1px;margin-bottom:18px}
  .goal-list{list-style:none;border-left:2px dotted var(--white);padding-left:16px;margin-left:0;margin-top:-3px}
  .goal-list li{color:var(--royal);font-weight:600;font-size:8.8px;line-height:12.2px;margin-bottom:12px}
  .goal-list li:last-child{margin-bottom:4px}
  .intro-band{position:absolute;left:0;top:0;width:209px;height:115px;background:var(--cyan);padding:20px 22px 0 22px}
  .intro-band .goal-list{padding-left:12px;height:60px}
  .intro-band .goal-list li{font-size:8.8px}
  .schedule{position:absolute;left:0;top:115px;width:209px;padding:24px 0 0 22px}
  .schedule-title{color:var(--orange);font-size:11.4px;font-weight:600;margin-bottom:14px}
  .event{display:flex;margin-bottom:12px}
  .event-date{width:33px;text-align:center;color:var(--orange);font-size:11.2px;line-height:14.5px;flex:none}
  .event-body{flex:1;padding-right:12px}
  .event-title{font-weight:600;font-size:8.8px;line-height:10.8px;color:var(--royal)}
  .event-time{color:var(--orange);font-size:7.6px;line-height:11px;margin-bottom:3px}
  .event-items{list-style:none;color:var(--sky);font-size:7.3px;line-height:10.7px}
  .schedule-cont{position:absolute;left:0;top:24px;width:209px;padding-left:22px}
  .schedule-cont .event{margin-bottom:13px}
  .guest-band{position:absolute;left:0;top:347px;width:209px;height:116px;background:var(--cyan);color:var(--white);font-weight:600;font-size:8.8px;line-height:12.1px;text-align:center;display:flex;align-items:center;justify-content:center;padding:0 18px}
</style>
</head>
<body>

<section class="spread spread--outside">
  <div class="panel panel--1 testimonials">
    <h2 class="section-title">What Community alumni are saying</h2>
    <p class="quote">“Leadership Brenvale was an awesome experience! I learned many interesting things about the county that I have lived in all my life. We had very informative panel discussions and the tours of local attractions, including the Oak Ridge Correctional Facility were eye opening! I enjoyed learning and working beside a great group of folks who are taking leadership roles in our communities to make our county a better place to live, work and play.”</p>
    <p class="attribution">Dana Whitlock, Co-Owner, Harbor Smokehouse</p>
    <p class="quote">“For the first year and a half I was working at Hartwell Pryor, I commuted from Seaford, so I was not involved in the community at all. Once we moved here, I knew I wanted and felt I had to become more involved. I learned about the program through a colleague. I couldn’t have asked for a better experience and it really exposed me to the many ways that I could get involved and contribute to the chamber and our community. I didn’t know a soul in that 2014 class when it started and now many of them are my very best friends. If you have an opportunity to go through Leadership Brenvale you would be crazy to pass it up. It is the best program the Chamber has and, quite frankly, one of the best opportunities to better yourself in this community.”</p>
    <p class="attribution">Grant R. Ellison, CPA,<br>Partner/Manager of the Millbrook Office Hartwell Pryor &amp; Associates, LLP</p>
  </div>

  <div class="panel panel--2 info">
    <h2 class="section-title">Attendance Policy</h2>
    <p>Attendance at all sessions including the opening retreat is compulsory. Participants may miss no more than one session to graduate; however, the <strong>Organizational Retreat is mandatory</strong>.</p>
    <h2 class="section-title">Tuition</h2>
    <p>If accepted in the Leadership Brenvale program, you or your employer/sponsor will be invoiced $400 for Chamber members and $500 for non-members. This fee covers costs for the retreat, classroom sessions, lunches, and graduation. No refunds will be provided for participants who drop out of the program or do not fulfill the required curriculum.</p>
    <h2 class="section-title">To Apply</h2>
    <p>Applications are available on the Chamber’s website, <strong>www.BrenvaleChamber.org</strong> Applications are due by November 2, 2020.</p>
    <p>Class size is limited. All applications received by the deadline will be reviewed and final participants for the Leadership Brenvale class will be contacted on December 4, 2020. However, all applicants will be notified of the status of their application in writing.</p>
    <p class="contact">For questions, please call the Chamber<br>555-014-2290</p>
    <div class="mini-name"><span class="dot" style="width:9px;height:9px"></span>Leadership Brenvale</div>
  </div>

  <div class="panel panel--3">
    <div class="cover-band">
      <p class="cover-quote">“The greatest wealth of a community lies not in the amount of its treasure, but in the quality of its leadership.”</p>
    </div>
    <div class="wordmark"><span class="dot" style="width:22px;height:22px"></span>Leadership Brenvale</div>
    <div class="sponsors">
      <b>SPONSORED BY</b><br>
      Lakeside Community College<br>
      Brenvale Chamber of Commerce and Tourism
    </div>
  </div>
</section>

<section class="spread spread--inside">
  <div class="panel panel--1">
    <div class="photo" role="img" aria-label="Group photo of program alumni standing together in a meeting room"></div>
    <div class="about">
      <p class="about-lead"><b>Leadership Brenvale</b> is a leadership certification program designed to prepare the leaders of tomorrow.</p>
      <p>During the five-month program, participants get an in-depth view of community issues, develop leadership skills necessary to assume leadership roles, and are exposed to community involvement opportunities.</p>
      <p>Leadership Brenvale will provide participants with the opportunities to:</p>
      <ul class="goal-list">
        <li>Build meaningful, long-lasting connections</li>
        <li>Establish ongoing dialogues with experienced community leaders</li>
        <li>Build and demonstrate leadership and communication skills</li>
      </ul>
    </div>
  </div>

  <div class="panel panel--2">
    <div class="intro-band">
      <ul class="goal-list"><li>Think critically about key business, policy, and civic issues facing Brenvale County</li></ul>
    </div>
    <div class="schedule">
      <h2 class="schedule-title">Schedule</h2>
      <div class="event">
        <div class="event-date">17<br>Jan</div>
        <div class="event-body">
          <h3 class="event-title">Organizational Retreat &amp; Dinner (Attendance Mandatory)</h3>
          <p class="event-time">10:00 a.m. – 7:00 p.m.</p>
          <ul class="event-items"><li>Introductions, Team Building, Motivation, Leadership Styles, Social Hour/ Dinner</li></ul>
        </div>
      </div>
      <div class="event">
        <div class="event-date">31<br>Jan</div>
        <div class="event-body">
          <h3 class="event-title">Business &amp; Industry</h3>
          <p class="event-time">8:30 a.m. – 4:00 p.m.</p>
          <ul class="event-items"><li>Business &amp; Industry Panel</li><li>Tour of Ironline Manufacturing facility</li><li>Tour of Keller Tool Company</li><li>“Taking your vision into B&amp;I”</li></ul>
        </div>
      </div>
      <div class="event">
        <div class="event-date">21<br>Feb</div>
        <div class="event-body">
          <h3 class="event-title">Education</h3>
          <p class="event-time">8:30 a.m. – 4:00 p.m.</p>
          <ul class="event-items"><li>Tour of selected programs at LCC</li><li>College Career Program overview</li><li>Lunch at Brenvale Career and College Academy</li><li>Tour of BCCA</li><li>Overview of CTE program paths</li></ul>
        </div>
      </div>
    </div>
  </div>

  <div class="panel panel--3">
    <div class="schedule-cont">
      <div class="event">
        <div class="event-date">14<br>Mar</div>
        <div class="event-body">
          <h3 class="event-title">Future Technologies &amp; Communications</h3>
          <p class="event-time">8:30 a.m. – 4:00 p.m.</p>
          <ul class="event-items"><li>LCC Presents interview</li><li>Trends and forecasts</li><li>Marketing &amp; communications panel</li></ul>
        </div>
      </div>
      <div class="event">
        <div class="event-date">4<br>Apr</div>
        <div class="event-body">
          <h3 class="event-title">Government</h3>
          <p class="event-time">8:30 a.m. – 4:00 p.m.</p>
          <ul class="event-items"><li>Overview of state/federal government</li><li>Overview of city/county government</li><li>Tour of Oak Ridge Correctional Institute</li><li>Tour of courthouse</li><li>Judicial presentations</li></ul>
        </div>
      </div>
      <div class="event">
        <div class="event-date">2<br>May</div>
        <div class="event-body">
          <h3 class="event-title">Health &amp; Wellness</h3>
          <p class="event-time">8:30 a.m. – 4:00 p.m.</p>
          <ul class="event-items"><li>Tour of Riverbend Hospice</li><li>Community Wellness Roundtable</li><li>Tour of Marlow Cancer Care Center</li><li>Virtual Medicine Tutorial</li><li>Tour of BRMC</li></ul>
        </div>
      </div>
      <div class="event">
        <div class="event-date">18<br>May</div>
        <div class="event-body">
          <h3 class="event-title">Graduation Ceremony and Luncheon</h3>
          <p class="event-time">12:00 p.m.</p>
        </div>
      </div>
    </div>
    <div class="guest-band">Participants are encouraged to invite their employer/supervisor/mentor/special guest (x2)</div>
  </div>
</section>

</body>
</html>
```